Book/Ebook Cover design for teen girls on purity/modesty
The Shape of Stillness: A Young Woman's Map to Quiet Strength
Book/Ebook Cover design for teen girls on purity/modesty - Books
Creative Brief
This book will be marketed to teenage girls, female family members like moms, grandmothers, aunts, etc., youth pastors, pastors, etc. I want a clean, fresh yet feminine look and feel. I envision an ornate mirror (handheld or otherwise) with the word "purity" being reflected on the mirror from the title. That is what's in my mind but I'm open to other ideas. Colors I like: aqua blue, bright green, and white.
Books
Feminine, fresh, charming, clean, modern.
This book will be published through Inkvale Press and Pagebrook. Full Bleed needed for the hard copy book. No less that 300 DPI. Need to know the basics about trim, margin, etc for book covers. RGB preferred.
tmerrow tmerrow
To Designers, I've uploaded an updated bio for myself for the back cover. I'll be choosing a winner very soon! Thank you so much for all your designs and hard work. I really appreciate it! Colette
FRIENDLY NOTE TO ALL DESIGNERS! Thanks for all your designs so far. Please do not include images of girls. I want the cover to draw girls from all backgrounds and an image of a girl whose skin color, hair and clothing makes a statement to one particular kind of girl. I want to make a statement to as many different kinds of girls as possible as the message is for them all. Also author name should either read "Colette J. Merrow" or "Colette Merrow". That's all for now. Please let me know how else I can help.
To all designers, Thanks for your willingness to create a design for my book! Size of book is 5.5X8.5. I'll need front and back cover designed. The mirror idea (described in the brief) is just something in my head. It can be pulled off believe but I'm also open to whatever fresh, clean and modern ideas you may have! Thanks again, tmerrow
Hi designers, It was brought to my attention that possibly the reason I haven't been getting many designers to commit is because this project isn't marked "guaranteed". I was under the impression that all projects were guaranteed. I do intend on picking a winner! I will call CS first thing Monday to see if I can change the project to read that it indeed is guaranteed. Until then, thanks so much for your submissions! I'm looking forward to picking one of your designs!
Dear designers, I would like to see some minimalistic designs. Simplistic but charming and feminine with a modern touch. Maybe the background the aqua blue color I like with a cute sketch of a mirror in white or with "purity" in a script font of some sort in the mirror. I'm not sure I'm going to like any of the random background kind of pictures. Thanks so much everyone. Tmerrow
Designers, The text for the back cover has not also been uploaded. Thanks!
To all designers, Thanks ahead of time for taking time to work on this project! I'm super excited to see what you all come up with. Please don't hesitate to ask questions or make suggestions. I have uploaded my head shot to use for the back cover. I am putting the finishing touches on the text for the back cover as well and will have that uploaded tonight or tomorrow. I'm not sure about how the ISBN will be printed on the book. Getting details on that as well. Thanks again! tmerrow

```html
<!DOCTYPE html>
<html lang="en">
<head>
<meta charset="utf-8">
<title>The Shape of Stillness — Book Cover</title>
<link href="https://fonts.googleapis.com/css2?family=Great+Vibes&family=Cormorant+Garamond:ital,wght@1,500&family=Montserrat:wght@500;600&family=Open+Sans:wght@400;600&display=swap" rel="stylesheet">
<style>
  :root {
    --backdrop: #3d3742;
    --cover: #d3ecf1;
    --cover-edge: #c3e1e8;
    --ink: #8c969a;
    --ink-dark: #5f6a6e;
    --title: #9aa4a8;
    --bloom-light: #eef8fa;
    --bloom-mid: #bfe0e8;
    --photo: #6b6260;
  }
  * { box-sizing: border-box; margin: 0; padding: 0; }
  html, body { width: 1200px; height: 901px; overflow: hidden; }
  body {
    background: var(--backdrop);
    display: flex;
    align-items: center;
    justify-content: center;
    gap: 40px;
    font-family: "Open Sans", sans-serif;
  }
  .cover {
    position: relative;
    width: 492px;
    height: 760px;
    background: var(--cover);
    border: 1px solid var(--cover-edge);
    color: var(--ink);
  }

  /* Back cover */
  .back { padding: 46px 44px 40px; }
  .back-heading { line-height: 1; margin-bottom: 26px; }
  .back-heading .lead {
    font-family: "Great Vibes", cursive;
    font-size: 40px;
    color: var(--ink-dark);
    display: block;
  }
  .back-heading .word {
    font-family: "Great Vibes", cursive;
    font-size: 74px;
    color: var(--title);
    display: block;
    margin-left: 60px;
  }
  .back-heading .tail {
    font-family: "Cormorant Garamond", serif;
    font-style: italic;
    font-size: 26px;
    color: var(--ink-dark);
    display: block;
    text-align: right;
  }
  .blurb {
    font-size: 12px;
    line-height: 1.6;
    text-align: justify;
    color: var(--ink-dark);
    margin-bottom: 22px;
  }
  .promise-title {
    font-size: 13px;
    font-weight: 600;
    color: var(--ink-dark);
    margin-bottom: 12px;
  }
  .promise-list { list-style: none; margin-bottom: 28px; }
  .promise-list li {
    position: relative;
    font-size: 11.5px;
    line-height: 1.5;
    color: var(--ink-dark);
    padding-left: 20px;
    margin-bottom: 10px;
  }
  .promise-list li::before {
    content: "";
    position: absolute;
    left: 4px; top: 6px;
    width: 6px; height: 6px;
    border-radius: 50%;
    background: var(--ink-dark);
  }
  .author-bio { display: flex; gap: 14px; align-items: flex-start; }
  .author-photo {
    flex: 0 0 74px;
    height: 90px;
    background: linear-gradient(160deg, #8a807c, var(--photo));
  }
  .author-bio p {
    font-size: 10.5px;
    line-height: 1.55;
    color: var(--ink-dark);
  }

  /* Front cover */
  .front-title {
    position: absolute;
    top: 56px; right: 36px;
    width: 380px;
    text-align: right;
  }
  .front-title .lead {
    font-family: "Cormorant Garamond", serif;
    font-style: italic;
    font-size: 24px;
    color: var(--title);
    display: block;
    margin-right: 150px;
  }
  .front-title .word {
    font-family: "Great Vibes", cursive;
    font-size: 104px;
    line-height: 0.95;
    color: var(--title);
    display: block;
  }
  .front-title .subtitle {
    font-family: "Cormorant Garamond", serif;
    font-style: italic;
    font-size: 16px;
    color: var(--ink);
    display: block;
    margin-top: 4px;
  }
  .bloom-art {
    position: absolute;
    left: 40px; top: 300px;
    width: 300px; height: 300px;
    border-radius: 50%;
    background: radial-gradient(circle at 50% 50%, var(--bloom-light) 0%, var(--bloom-mid) 55%, rgba(211,236,241,0) 72%);
  }
  .author-name {
    position: absolute;
    right: 36px; bottom: 72px;
    font-family: "Montserrat", sans-serif;
    font-weight: 600;
    font-size: 24px;
    letter-spacing: 2px;
    color: var(--title);
  }
</style>
</head>
<body>
  <section class="cover back" aria-label="Back cover">
    <h2 class="back-heading">
      <span class="lead">What does</span>
      <span class="word">Stillness</span>
      <span class="tail">look like?</span>
    </h2>
    <p class="blurb">In a world that never stops talking, a quiet heart can feel out of place. This gentle guide walks with you through the noise of pressure, comparison and hurry, and shows how calm confidence grows from knowing who you are and whose you are. Each chapter offers honest stories, simple practices and space to reflect, so you can choose your path with peace.</p>
    <h3 class="promise-title">The Shape of Stillness will:</h3>
    <ul class="promise-list">
      <li>Help you name the pressures you face and set them down.</li>
      <li>Guide you through honest talks about friendship, worth and choices.</li>
      <li>Offer short daily practices to build calm and courage.</li>
      <li>Remind you that your heart was made to bloom in its own time.</li>
    </ul>
    <div class="author-bio">
      <div class="author-photo" role="img" aria-label="Author portrait photograph"></div>
      <p>Colette Merrow is a speaker and youth mentor who loves helping young women find their voice. She lives with her family and writes from her kitchen table.</p>
    </div>
  </section>

  <section class="cover front" aria-label="Front cover">
    <h1 class="front-title">
      <span class="lead">The Shape of</span>
      <span class="word">Stillness</span>
      <span class="subtitle">A Young Woman's Map to Quiet Strength</span>
    </h1>
    <div class="bloom-art" role="img" aria-label="Soft pale roses illustration"></div>
    <p class="author-name">COLETTE J. MERROW</p>
  </section>
</body>
</html>
```